New look modernised front page for Pellmark Sporting League Website Which incorporates our new logo (to be provided as a png file)
We want the home page to a panel to allow an image rotator and provide ready access to links to other inflation via some link menus/panel/button
1. Join a Croquet Club - links to details about Croquet in NSW - gateway to information of interest or the general public/“interested others” eg about the game, clubs locations and contacts
2. Club and Member Information - newsletters, Calender of events, and downloads
3. Officials and volunteers - training resources etc
4. Member and Club sign in - access to database
5. About Us - information about Pellmark Sporting League incorporated -peak body for croquet in NSW - governance, contact details etc

Current website is at https://www.pellmark-league.org/index.html

Target Market(s)

Dual target - People interested in learning about croquet and existing members

Number of Pages Required

1 page

Font styles to use
Sans Serif

Colors
0255a3
3377b5
85acd3
85cae6
33a6d7
0792cd
00a990

Requirements
Must have
• Contemporary feel
• Include logo - file attached
• Colours to include blues which are the NSW colour
Nice to have
• We want the home page to a panel to allow an image rotator and provide ready access to links to other inflation via some link menus/panel/button
• 1. Join a Croquet Club - links to details about Croquet in NSW - gateway to information of interest or the general public/“interested others” eg about the game, clubs locations and contacts
• 2. Club and Member Information - newsletters, Calender of events, and downloads
• 3. Officials and volunteers - training resources etc
• 4. Member and Club sign in - access to database
• 5. About Us - information about Pellmark Sporting League incorporated -peak body for croquet in NSW - governance, contact details etc
• Want to have feeling of activity/movement/alive
• Current website is at https://www.pellmark-league.org/index.html
• Some photos attached for information

```html
<!DOCTYPE html>
<html lang="en">
<head>
<meta charset="utf-8">
<title>Pellmark Sporting League</title>
<link rel="stylesheet" href="https://fonts.googleapis.com/css2?family=Open+Sans:wght@400;600;700&family=Roboto:wght@300;400;500&family=Roboto+Condensed:wght@400;700&display=swap">
<style>
:root{
  --navy:#0255a3;
  --blue:#3377b5;
  --sky:#33a6d7;
  --cyan:#0792cd;
  --green:#00a990;
  --ink:#1d1d1d;
  --text:#555;
  --pale-blue:#e2f3f8;
  --pale-mint:#e3f8f7;
  --footer:#0d0d0d;
}
*{margin:0;padding:0;box-sizing:border-box}
html,body{width:1200px;height:3742px;overflow:hidden}
body{font-family:"Open Sans",Arial,sans-serif;color:var(--ink);background:#fff;position:relative}
.btn{position:absolute;display:flex;align-items:center;justify-content:center;border-radius:20px;font-size:15px;font-family:"Open Sans",sans-serif}
.btn-green{background:var(--green);color:#fff}
.btn-inline{position:static}

/* header */
.site-header{position:absolute;left:0;top:0;width:1200px;height:122px;background:#fff}
.brand{position:absolute;left:87px;top:38px;display:flex;align-items:center;gap:14px}
.brand-mark{width:30px;height:44px;background:var(--navy)}
.brand-name{font-family:"Roboto Condensed",sans-serif;font-weight:700;font-size:38px;color:var(--ink)}
.phone{position:absolute;left:679px;top:50px;font-size:21px;color:var(--ink);display:flex;align-items:center;gap:6px}
.btn-member{left:831px;top:43px;width:142px;height:39px}
.btn-club{left:983px;top:43px;width:125px;height:39px;border:1.5px solid var(--blue);color:var(--navy);background:#fff}

/* nav */
.main-nav{position:absolute;left:0;top:122px;width:1200px;height:53px;background:linear-gradient(#33a6d7,#0792cd 60%,#0468a8)}
.main-nav ul{list-style:none;display:flex;position:absolute;left:87px;top:0;height:53px}
.main-nav li{color:#fff;font-size:18px;font-family:"Roboto",sans-serif;height:53px;display:flex;align-items:center;padding:0 22px}
.main-nav li.active{background:var(--green);width:130px;justify-content:center}

/* hero */
.hero{position:absolute;left:0;top:175px;width:1200px;height:630px}
.hero-photo{position:absolute;inset:0;background:linear-gradient(160deg,#4f7a3a 0%,#7e9a4a 35%,#a9b567 60%,#8ca454 100%)}
.hero-curve{position:absolute;left:0;bottom:0}
.hero-caption{position:absolute;left:87px;top:175px;width:430px;height:195px;background:rgba(20,25,30,.55);border-radius:6px;padding:18px 26px}
.hero-caption h1{font-family:"Roboto Condensed",sans-serif;font-weight:400;font-size:58px;color:#fff;line-height:1.1}
.hero-caption p{font-family:"Roboto Condensed",sans-serif;font-size:22px;color:#fff;margin-top:6px}
.btn-join{left:31px;top:136px;width:182px;height:38px;font-size:17px;font-family:"Roboto Condensed",sans-serif}
.slider-dots{position:absolute;left:1156px;top:205px;display:flex;flex-direction:column;gap:14px}
.slider-dots span{width:9px;height:9px;border-radius:50%;background:#fff}
.slider-dots span.on{background:var(--sky)}

/* about */
.about-frame{position:absolute;left:87px;top:916px;width:380px;height:319px;border:3px solid #555}
.about-block{position:absolute;left:105px;top:935px;width:400px;height:322px;background:var(--navy)}
.about-photo{position:absolute;left:125px;top:948px;width:400px;height:330px;background:linear-gradient(150deg,#6a8d5a,#c7b88a 55%,#8ba070)}
.about-text{position:absolute;left:579px;top:950px;width:548px}
h2.title{font-family:"Roboto",sans-serif;font-weight:400;font-size:40px;color:var(--ink)}
.subtitle{font-family:"Roboto",sans-serif;font-size:17px;font-weight:500;margin-top:6px;color:#222}
.body-copy{font-size:13px;line-height:28px;color:var(--text);margin-top:8px}
.btn-more{width:102px;height:30px;font-size:13px;margin-top:10px}

/* training */
.training{position:absolute;left:0;top:1407px;width:1200px;height:693px;background:var(--pale-blue)}
.section-title{position:absolute;left:0;width:1200px;text-align:center;font-family:"Roboto",sans-serif;font-size:38px;font-weight:400;color:var(--ink)}
.resource-card{position:absolute;width:413px;height:204px;border-radius:8px;overflow:hidden;border-bottom:8px solid var(--green)}
.resource-card .img{position:absolute;inset:0}
.resource-card h3{position:absolute;left:0;right:0;bottom:16px;text-align:center;color:#fff;font-family:"Open Sans",sans-serif;font-weight:600;font-size:24px;text-shadow:0 1px 3px rgba(0,0,0,.6)}

/* coaching */
.coaching-box{position:absolute;left:102px;top:2246px;width:634px;height:344px;border:2px solid #333}
.coaching-text{position:absolute;left:148px;top:2296px;width:475px}
.coaching-text h2{font-family:"Roboto",sans-serif;font-weight:400;font-size:30px}
.coaching-text p{font-size:13px;line-height:24px;color:var(--text);margin-top:6px;text-align:justify}
.btn-download{width:109px;height:32px;font-size:13px;margin-top:10px}
.coaching-photo{position:absolute;left:656px;top:2266px;width:437px;height:304px;background:linear-gradient(160deg,#8a7d5b,#b7a67a 50%,#6d6550);box-shadow:0 6px 14px rgba(0,0,0,.35)}

/* events */
.events{position:absolute;left:0;top:2745px;width:1200px;height:598px;background:var(--pale-mint)}
.event-card{position:absolute;top:182px;width:316px}
.event-card .img{width:316px;height:192px;border:4px solid #fff;box-shadow:0 1px 4px rgba(0,0,0,.25);position:relative}
.date-badge{position:absolute;left:4px;top:4px;width:44px;height:46px;background:var(--green);color:#fff;text-align:center;font-family:"Roboto",sans-serif;line-height:1}
.date-badge b{display:block;font-size:20px;font-weight:400;padding-top:6px}
.date-badge small{font-size:10px}
.event-card h3{font-family:"Roboto",sans-serif;font-weight:400;font-size:20px;margin-top:18px;color:#222}
.event-card p{font-size:13px;line-height:22px;color:#444;margin-top:6px;padding-left:4px}
.event-card a{display:block;font-size:13px;color:var(--cyan);margin-top:8px;text-decoration:none}

/* footer */
.footer-stripe{position:absolute;left:0;top:3343px;width:1200px;height:10px;background:var(--blue)}
.site-footer{position:absolute;left:0;top:3353px;width:1200px;height:389px;background:var(--footer);color:#fff}
.footer-col{position:absolute;top:84px}
.footer-col h4{font-family:"Roboto",sans-serif;font-weight:400;font-size:23px;letter-spacing:.3px}
.footer-col ul{list-style:none;margin-top:20px}
.footer-col li{font-size:15px;line-height:33px}
.contact-item{display:flex;gap:12px;margin-top:22px}
.contact-item b{font-size:15px;font-weight:600;display:block}
.contact-item span{font-size:14px}
.newsletter-input{position:absolute;left:793px;top:132px;width:295px;height:48px;border:1px solid #ccc;font-size:15px;padding:14px 14px}
.btn-subscribe{left:793px;top:187px;width:295px;height:48px;border-radius:0;font-size:18px}
.footer-rule{position:absolute;left:90px;top:312px;width:1020px;height:1px;background:#444}
.copyright{position:absolute;left:0;top:352px;width:1200px;text-align:center;font-size:14px;color:#ccc}
</style>
</head>
<body>

<header class="site-header">
  <div class="brand"><span class="brand-mark"></span><span class="brand-name">Pellmark Sporting League</span></div>
  <div class="phone">
    <svg width="18" height="18" viewBox="0 0 24 24"><path fill="#0792cd" d="M6.6 10.8a15 15 0 0 0 6.6 6.6l2.2-2.2c.3-.3.7-.4 1-.2 1.1.4 2.3.6 3.6.6.6 0 1 .4 1 1V20c0 .6-.4 1-1 1A17 17 0 0 1 3 4c0-.6.4-1 1-1h3.5c.6 0 1 .4 1 1 0 1.3.2 2.5.6 3.6.1.3 0 .7-.2 1z"/></svg>
    0855010237
  </div>
  <div class="btn btn-green btn-member">Member sign in</div>
  <div class="btn btn-club">Club sign in</div>
</header>

<nav class="main-nav">
  <ul>
    <li class="active">Home</li><li>About us</li><li>How to Play</li><li>Clubs</li><li>Coaching</li><li>Refereeing</li><li>Shop</li><li>Events</li><li>Contact</li>
  </ul>
</nav>

<section class="hero">
  <div class="hero-photo" role="img" aria-label="Player striking a croquet ball with a mallet on a grass lawn"></div>
  <svg class="hero-curve" width="1200" height="90" viewBox="0 0 1200 90">
    <path d="M0 0 Q600 130 1200 0 L1200 90 L0 90Z" fill="#fff"/>
    <path d="M0 0 Q600 130 1200 0 Q600 95 0 0Z" fill="#00a990"/>
  </svg>
  <div class="hero-caption">
    <h1>Croquet in NSW</h1>
    <p>The Pellmark Players' Association Inc</p>
    <div class="btn btn-green btn-join">Join a Croquet Club</div>
  </div>
  <div class="slider-dots"><span class="on"></span><span></span><span></span><span></span></div>
</section>

<section class="about">
  <div class="about-frame"></div>
  <div class="about-block"></div>
  <div class="about-photo" role="img" aria-label="Group of club members in sports clothing standing on a croquet lawn"></div>
  <div class="about-text">
    <h2 class="title">About us</h2>
    <p class="subtitle">Neque porro quisquam est qui dolorem</p>
    <p class="body-copy">It is a long established fact that a reader will be distracted by the readable content of a page when looking at its layout. The point of using Lorem Ipsum is that it has a more-or-less normal distribution of letters, as opposed to using 'Content here, content here', making it look like readable English. Many desktop publishing packages and web page editors now use Lorem Ipsum as their default model text, and a search for 'lorem ipsum' will uncover many web sites still in their infancy.</p>
    <div class="btn btn-green btn-inline btn-more">Read More</div>
  </div>
</section>

<section class="training">
  <h2 class="section-title" style="top:78px">Training Resources</h2>
  <div class="resource-card" style="left:165px;top:160px"><div class="img" role="img" aria-label="Players on a croquet lawn during a training session" style="background:linear-gradient(160deg,#56703f,#8fa864)"></div><h3>Porro quisquam</h3></div>
  <div class="resource-card" style="left:609px;top:160px"><div class="img" role="img" aria-label="Croquet balls and a hoop on green grass" style="background:linear-gradient(160deg,#2f5a2a,#4d7d3a)"></div><h3>Dolorem ipsum</h3></div>
  <div class="resource-card" style="left:165px;top:387px"><div class="img" role="img" aria-label="Coach guiding a player's mallet swing" style="background:linear-gradient(160deg,#6c8460,#a6ae86)"></div><h3>Dolorem ipsum</h3></div>
  <div class="resource-card" style="left:609px;top:387px"><div class="img" role="img" aria-label="Two players shaking hands after a game" style="background:linear-gradient(160deg,#3d4a35,#7f9060)"></div><h3>Porro quisquam</h3></div>
</section>

<section class="coaching">
  <div class="coaching-box"></div>
  <div class="coaching-text">
    <h2>Coaching</h2>
    <p>It is a long established fact that a reader will be distracted by the readable content of a page when looking at its layout. The point of using Lorem Ipsum is that it has a more-or-less normal distribution of letters, as opposed to using 'Content here, content here', making it look like readable English. Many desktop publishing packages and web page editors now use Lorem Ipsum as their default model text, and a search for</p>
    <div class="btn btn-green btn-inline btn-download">Downloads</div>
  </div>
  <div class="coaching-photo" role="img" aria-label="Young players posing with mallets beside a croquet equipment cart"></div>
</section>

<section class="events">
  <h2 class="section-title" style="top:90px">Events</h2>
  <article class="event-card" style="left:90px">
    <div class="img" role="img" aria-label="Players in a match on a croquet lawn" style="background:linear-gradient(160deg,#4e6e39,#9aae6a)"><div class="date-badge"><b>02</b><small>JUN</small></div></div>
    <h3>Neque porro quisquam</h3>
    <p>It has survived not only five centuries, but also the leap into electronic typesetting,</p>
    <a>Read More »</a>
  </article>
  <article class="event-card" style="left:439px">
    <div class="img" role="img" aria-label="Croquet balls, mallet and a scorecard on grass" style="background:linear-gradient(160deg,#6a7b4a,#b5ac7c)"><div class="date-badge"><b>02</b><small>JUN</small></div></div>
    <h3>Dolorem ipsum quia</h3>
    <p>It has survived not only five centuries, but also the leap into electronic typesetting, remaining</p>
    <a>Read More »</a>
  </article>
  <article class="event-card" style="left:788px">
    <div class="img" role="img" aria-label="Championship participants gathered behind a welcome banner" style="background:linear-gradient(160deg,#6d8fb8,#c9c9c0 60%,#7f9a6a)"><div class="date-badge"><b>02</b><small>JUN</small></div></div>
    <h3>Ipsum quia dolor sit amet,</h3>
    <p>It has survived not only five centuries, but also the leap into electronic typesetting, remaining</p>
    <a>Read More »</a>
  </article>
</section>

<div class="footer-stripe"></div>
<footer class="site-footer">
  <div class="footer-col" style="left:92px">
    <h4>CONTACT US</h4>
    <div class="contact-item" style="margin-top:26px">
      <svg width="20" height="16" viewBox="0 0 20 16"><rect x="1" y="1" width="18" height="14" fill="none" stroke="#fff" stroke-width="1.6"/><path d="M1 1l9 7 9-7" fill="none" stroke="#fff" stroke-width="1.6"/></svg>
      <div><b>EMAIL ADDRESS</b><span>info@pellmark-league.org</span></div>
    </div>
    <div class="contact-item">
      <svg width="20" height="20" viewBox="0 0 24 24"><path fill="none" stroke="#fff" stroke-width="1.6" d="M6.6 10.8a15 15 0 0 0 6.6 6.6l2.2-2.2c.3-.3.7-.4 1-.2 1.1.4 2.3.6 3.6.6.6 0 1 .4 1 1V20c0 .6-.4 1-1 1A17 17 0 0 1 3 4c0-.6.4-1 1-1h3.5c.6 0 1 .4 1 1 0 1.3.2 2.5.6 3.6.1.3 0 .7-.2 1z"/></svg>
      <div><b>PHONE NUMBER</b><span>(555) 010-4818</span></div>
    </div>
  </div>
  <div class="footer-col" style="left:387px">
    <h4>ABOUT</h4>
    <ul><li>Home</li><li>About Us</li><li>Services</li><li>How to Play</li></ul>
  </div>
  <div class="footer-col" style="left:564px">
    <h4>RESOURCES</h4>
    <ul><li>Support</li><li>Why Us</li><li>Testimonials</li><li>FAQ</li></ul>
  </div>
  <div class="footer-col" style="left:791px"><h4>NEWSLETTERS</h4></div>
  <div class="newsletter-input">Email address</div>
  <div class="btn btn-green btn-subscribe">Subscribe Now</div>
  <div class="footer-rule"></div>
  <p class="copyright">© 2018 Company Name &nbsp;All right reserved</p>
</footer>

</body>
</html>
```